Consulting, Investors, Joint Venture Website

Founded in April 2018, Marendo Consultants Limited (MCL) is an advisory consulting firm specializing in engaging investors in business ventures in Tanzania.
With extensive experience in construction, energy, oil and gas and the legal professions, our team assembles our expertise that allows foreign investors to set foot and flourish in the Tanzanian market.
MCL is locally owned, founded and registered. Our shareholders are cultured Tanzanian citizens with extensive corporate experience in South Africa, Tanzania, United Kingdom and the United States.

Our mission is to provide responsive and unrivalled professional advice from learned and experienced professionals versed in the local market, with an understanding of the cultural and logistical challenges faced by foreign investors.

Our vision is to provide a complete investor’s package that initiates with company registration, compliance and documentation services and ultimately operational facilitation services.

Target Market(s)

Foreign Investors, International companies

Industry/Entity Type

Business Consultant

Number of Pages Required

5+ page

Requirements
Must have
• It will be 5 pages - Home, About Us, Services, Portfolio, Contact Us
Nice to have
• if it can look like https://www.plorvex.example/
• or https://www.dunetri.example or http://www.quillbrook.example/

```html
<!DOCTYPE html>
<html lang="en">
<head>
<meta charset="utf-8">
<title>Marendo Consultants Limited — Home</title>
<link href="https://fonts.googleapis.com/css2?family=Lato:wght@400;700&family=Spectral:wght@500;600&display=swap" rel="stylesheet">
<style>
  :root {
    --ink: #141416;
    --ink-soft: #1c1c1f;
    --paper: #ffffff;
    --accent: #1a7fd1;
    --muted: #9a9aa2;
    --line: #3a3a40;
    --text-light: #e9e9ee;
    --tone-blue: #16344f;
    --tone-amber: #4a2c1a;
  }
  * { box-sizing: border-box; margin: 0; padding: 0; }
  html, body { width: 1200px; height: 773px; overflow: hidden; background: var(--paper); }
  body { position: relative; font-family: "Lato", sans-serif; color: var(--text-light); }

  .hero { position: absolute; left: 0; top: 0; width: 1120px; height: 600px; background: var(--ink); overflow: hidden; }
  .hero-tail { position: absolute; left: 600px; top: 600px; width: 520px; height: 100px; background: var(--ink); border-bottom: 2px solid var(--accent); }
  .side-rail { position: absolute; left: 1120px; top: 0; width: 80px; height: 520px; background: var(--ink); }

  .hero-visual {
    position: absolute; left: 0; top: 0; width: 1120px; height: 600px;
    background: linear-gradient(160deg, var(--ink) 0%, var(--tone-blue) 45%, var(--tone-amber) 70%, var(--ink) 100%);
    opacity: 0.55;
  }

  .brand { position: absolute; left: 40px; top: 34px; display: flex; align-items: center; gap: 10px; }
  .brand-dot { width: 22px; height: 22px; border-radius: 50%; background: var(--accent); }
  .brand-name { font-size: 17px; font-weight: 700; letter-spacing: 1.5px; text-transform: uppercase; color: var(--text-light); }

  .main-nav { position: absolute; left: 560px; top: 40px; display: flex; gap: 34px; font-size: 12px; }
  .main-nav a { color: var(--text-light); text-decoration: none; }
  .main-nav a.is-active { color: var(--accent); }

  .rail-line { position: absolute; left: 1085px; top: 0; width: 1px; height: 470px; background: var(--line); }
  .rail-accent { position: absolute; left: 1084px; width: 3px; height: 40px; background: var(--accent); }
  .language { position: absolute; left: 1098px; top: 30px; font-size: 10px; letter-spacing: 1px; color: var(--text-light); white-space: nowrap; }
  .language b { color: var(--accent); }
  .language::before { content: ""; position: absolute; left: -70px; top: 6px; width: 60px; height: 1px; background: var(--line); }

  .rail-text { position: absolute; left: 1100px; font-size: 10px; letter-spacing: 1px; text-transform: uppercase; color: var(--text-light); writing-mode: vertical-rl; white-space: nowrap; }
  .rail-email { top: 120px; }
  .rail-phone { top: 320px; }

  .scroll-cue { position: absolute; left: 1120px; top: 520px; width: 80px; height: 180px; background: var(--paper); }
  .scroll-cue span { position: absolute; left: 32px; top: 24px; writing-mode: vertical-rl; font-size: 10px; letter-spacing: 1.5px; color: #333; text-transform: uppercase; }
  .scroll-cue::after { content: ""; position: absolute; left: 0; top: 0; width: 1px; height: 180px; background: #e1e1e6; }

  .hero-copy { position: absolute; left: 140px; top: 360px; }
  .hero-eyebrow { font-size: 13px; color: var(--text-light); margin-bottom: 10px; }
  .hero-title { font-family: "Spectral", serif; font-weight: 600; font-size: 42px; line-height: 1.18; color: #fff; }
  .btn { display: inline-flex; align-items: center; gap: 10px; margin-top: 34px; background: var(--accent); color: #fff; font-size: 10px; font-weight: 700; letter-spacing: 1px; text-transform: uppercase; padding: 11px 16px; text-decoration: none; }

  .section-tabs { position: absolute; left: 40px; top: 640px; display: flex; gap: 70px; }
  .tab { display: flex; align-items: center; gap: 10px; font-size: 12px; color: var(--muted); padding-bottom: 22px; position: relative; }
  .tab-num { width: 26px; height: 26px; border: 1px solid #cfcfd6; border-radius: 50%; display: flex; align-items: center; justify-content: center; font-size: 9px; color: var(--muted); }
  .tab.is-active { color: #222; }
  .tab.is-active .tab-num { border-color: var(--accent); color: var(--accent); }
  .tab.is-active::after { content: ""; position: absolute; left: 0; bottom: 0; width: 120px; height: 2px; background: var(--accent); }
</style>
</head>
<body>
  <section class="hero">
    <div class="hero-visual" role="img" aria-label="Hero photograph: abstract multicoloured light streaks on a dark background"></div>

    <div class="brand">
      <span class="brand-dot"></span>
      <span class="brand-name">Marendo Consultants</span>
    </div>

    <nav class="main-nav">
      <a href="#" class="is-active">Home</a>
      <a href="#">About</a>
      <a href="#">Services</a>
      <a href="#">Portfolio</a>
      <a href="#">Contact</a>
    </nav>

    <div class="hero-copy">
      <p class="hero-eyebrow">Marendo Consultants</p>
      <h1 class="hero-title">We get you the results you<br>have only dreamt of reaching.</h1>
      <a href="#" class="btn">Learn more
        <svg width="16" height="8" viewBox="0 0 16 8"><path d="M0 4h14M11 1l3 3-3 3" stroke="#fff" fill="none" stroke-width="1.2"/></svg>
      </a>
    </div>
  </section>

  <div class="side-rail"></div>
  <div class="hero-tail"></div>

  <div class="rail-line"></div>
  <div class="rail-accent" style="top:60px"></div>
  <div class="rail-accent" style="top:420px"></div>
  <p class="language">Language: <b>ENG</b></p>
  <p class="rail-text rail-email">info@marendo.example</p>
  <p class="rail-text rail-phone">+255 22 410 7788</p>

  <div class="scroll-cue"><span>Scroll down</span></div>

  <nav class="section-tabs">
    <div class="tab is-active"><span class="tab-num">01</span>Marendo Consultants</div>
    <div class="tab"><span class="tab-num">02</span>Our Services</div>
    <div class="tab"><span class="tab-num">03</span>Portfolio</div>
  </nav>
</body>
</html>
```